Investment website design - investing in mutual funds

I need a design of a website (only homepage for now) dedicated to investment in mutual funds. Attached is a mock up with all the elements the homepage design should contain. The homepage should contain a logo in the upper left corner, the domain the website will run on is www.morvatelsko.cz , in the upper right corner there should be 2 buttons or links SIGN UP / SIGN IN. The bottom of the homepage should contain links to ABOUT US, FAQ, PRIVACY POLICY, CONTACT US.
Now the main elements on the homepage
1) Video that will explain how the investment works exactly, under this video we will have 3 illustrated icons like the ones attached (see 2nd attachement) that will show the potential investor what exactly they could get when investing with us (education for kids, happy life after they retire, regular monthly payment for the rest of their life).
2) On the right side next to the video we will have a calculator where a potential investor can play with the numbers, the investor can fill in the MONTHLY PAYMENT that he wants to invest regularly every month, the time frame of the investment - for how long he wants to invest. Once the potential investor selects those 2 variables we will calculate for him 2 options - either he can get a ONE TIME PAYOUT once he reaches his investment horizon or he can get a regular monthly payment for the rest of his life. Under the laculator there will be a button 'I want to invest ->'. The functionality of the calculator should be similar to the calculator that can be found here http://www.brovikbanka.cz/brovik-podilove-fondy/ and https://pelvaro.cz/.
The design should look similar to https://pelvaro.cz/ (font, colors, logo). We prefer white background in the area where we have the video and calculator. We also like the design of www.truvanex.com. Let me know if you have any questions.

```html
<!DOCTYPE html>
<html lang="en">
<head>
<meta charset="utf-8">
<title>Morvatelsko – Investing in mutual funds</title>
<link rel="stylesheet" href="https://fonts.googleapis.com/css2?family=Open+Sans:wght@400;600&family=Roboto:wght@400;500;700&display=swap">
<style>
:root{
  --brand:#1a8fb0;
  --blue:#0f72bd;
  --teal:#1f9bb6;
  --slider:#17a9a6;
  --track:#b5b5b5;
  --ink:#222;
  --muted:#333;
  --line:#9a9a9a;
  --page:#f4f4f5;
  --footer:#1a1a1a;
  --white:#fff;
}
*{box-sizing:border-box;margin:0;padding:0}
html,body{width:1200px;height:927px;overflow:hidden}
body{position:relative;font-family:"Open Sans",Arial,sans-serif;color:var(--ink);
  background:linear-gradient(160deg,#f0f0f1 0%,#f8f8f8 40%,#f1f1f2 70%,#f7f7f7 100%)}
.site-header{position:absolute;left:0;top:0;width:1200px;height:96px;background:var(--white);
  box-shadow:0 2px 10px rgba(0,0,0,.08)}
.brand{position:absolute;left:92px;top:30px;font-family:"Roboto",Arial,sans-serif;font-weight:700;
  font-size:33px;letter-spacing:1px;color:var(--brand);text-transform:uppercase}
.auth{position:absolute;left:903px;top:25px;display:flex;gap:4px}
.auth a{display:block;width:103px;height:41px;line-height:40px;text-align:center;color:var(--white);
  text-decoration:none;font-size:19px;border-radius:2px}
.auth .sign-in{background:var(--blue)}
.auth .sign-up{background:var(--teal)}
.section-title{position:absolute;left:90px;top:193px;font-family:"Roboto",Arial,sans-serif;
  font-weight:400;font-size:24px;color:var(--ink)}
.video{position:absolute;left:92px;top:239px;width:470px;height:281px;background:#000}
.video svg{display:block}
.benefits{position:absolute;left:0;top:0}
.benefit{position:absolute;width:140px;text-align:center;font-family:"Roboto",Arial,sans-serif;
  font-size:19px;line-height:25px;color:var(--ink)}
.benefit .art{display:block;width:90px;height:90px;border-radius:50%;margin:0 auto 12px;
  border:2px solid #d8d8d8;box-shadow:0 1px 3px rgba(0,0,0,.15)}
.art.kids{background:radial-gradient(circle at 50% 55%,#f6c77a,#f2e4d0 60%,#fff)}
.art.income{background:radial-gradient(circle at 50% 60%,#e8c845,#eef2e6 60%,#fff)}
.art.retire{background:radial-gradient(circle at 50% 50%,#d6a86a,#b9bccb 65%,#c9cad4)}
.calculator{position:absolute;left:598px;top:197px;width:515px;height:505px;background:var(--white);
  border:1px solid #cfcfcf;box-shadow:0 2px 8px rgba(0,0,0,.08)}
.calculator h2{position:absolute;left:28px;top:32px;font-family:"Roboto",Arial,sans-serif;
  font-weight:400;font-size:24px;color:var(--ink)}
.field{position:absolute;left:28px;width:458px;height:44px;border:1px solid var(--line);
  padding-left:14px;line-height:42px;font-size:14.5px;color:var(--muted)}
.label{position:absolute;left:28px;font-size:14.5px;color:var(--muted)}
.range{position:absolute;left:31px;top:190px}
.range-ends{position:absolute;left:31px;top:207px;width:450px;display:flex;justify-content:space-between;
  font-size:13.5px;color:var(--muted)}
.or{position:absolute;left:0;width:100%;top:316px;text-align:center;font-size:13.5px;color:var(--muted)}
.invest{position:absolute;left:296px;top:410px;width:190px;height:39px;line-height:39px;text-align:center;
  background:var(--blue);color:var(--white);font-family:"Roboto",Arial,sans-serif;font-size:19px;
  border-radius:2px;text-decoration:none}
.site-footer{position:absolute;left:0;top:806px;width:1200px;height:121px;background:var(--footer);
  color:#f2f2f2;text-align:center;font-size:14.5px}
.footer-nav{position:absolute;top:35px;width:100%}
.footer-nav a{color:#f2f2f2;text-decoration:none}
.footer-nav .sep{margin:0 8px}
.copyright{position:absolute;top:70px;width:100%}
</style>
</head>
<body>
<header class="site-header">
  <div class="brand">Morvatelsko</div>
  <nav class="auth">
    <a class="sign-in" href="#">Sign in</a>
    <a class="sign-up" href="#">Sign up</a>
  </nav>
</header>

<h1 class="section-title">Video about our product</h1>

<div class="video">
  <svg width="470" height="281" viewBox="0 0 470 281">
    <rect x="0" y="0" width="470" height="25" fill="#000"/>
    <g fill="#fff">
      <circle cx="428" cy="12" r="2.3"/><circle cx="420" cy="7.5" r="2.3"/><circle cx="420" cy="16.5" r="2.3"/>
      <path d="M420 7.5 L428 12 L420 16.5" stroke="#fff" stroke-width="1.4" fill="none"/>
      <circle cx="451" cy="12" r="6.5"/>
    </g>
    <rect x="450" y="10" width="2" height="6" fill="#000"/><rect x="450" y="7" width="2" height="2" fill="#000"/>
    <defs>
      <linearGradient id="scene" x1="0" y1="0" x2="1" y2="1">
        <stop offset="0" stop-color="#2aa6c3"/><stop offset="1" stop-color="#1a8fb0"/>
      </linearGradient>
    </defs>
    <rect x="0" y="25" width="470" height="225" fill="url(#scene)" role="img" aria-label="Illustration of a businessman with a briefcase and magnifying glass over a city skyline and rising chart"/>
    <rect x="198" y="114" width="74" height="52" rx="10" fill="#222" opacity=".85"/>
    <path d="M228 129 L228 151 L246 140 Z" fill="#fff"/>
    <rect x="0" y="250" width="470" height="31" fill="#1b1b1b"/>
    <rect x="0" y="250" width="470" height="5" fill="#555"/>
    <circle cx="7" cy="253" r="5" fill="#ddd"/>
    <path d="M20 263 L20 275 L31 269 Z" fill="#bbb"/>
    <path d="M55 266 h3 l4 -4 v14 l-4 -4 h-3 z" fill="#bbb"/>
    <circle cx="431" cy="269" r="5" fill="#bbb"/>
    <g stroke="#bbb" stroke-width="1.6" fill="none">
      <path d="M448 266 v-4 h4"/><path d="M462 262 h4 v4"/><path d="M448 272 v4 h4"/><path d="M466 272 v4 h-4"/>
    </g>
  </svg>
</div>

<div class="benefits">
  <div class="benefit" style="left:97px;top:544px">
    <span class="art kids" role="img" aria-label="Illustration of a child reading books"></span>
    Education<br>for kids
  </div>
  <div class="benefit" style="left:251px;top:545px">
    <span class="art income" role="img" aria-label="Illustration of a tap dripping coins onto money"></span>
    Passive<br>income
  </div>
  <div class="benefit" style="left:405px;top:548px">
    <span class="art retire" role="img" aria-label="Illustration of a retired couple"></span>
    Happy<br>retirement
  </div>
</div>

<section class="calculator">
  <h2>Our Online Calculator</h2>
  <div class="field" style="top:87px">Regular monthly investment</div>
  <div class="label" style="top:156px">Length of investment</div>
  <svg class="range" width="454" height="16" viewBox="0 0 454 16">
    <rect x="0" y="4" width="450" height="8" rx="4" fill="var(--track)"/>
    <rect x="0" y="4" width="136" height="8" rx="4" fill="var(--slider)"/>
    <rect x="133" y="0" width="7" height="16" rx="3.5" fill="var(--slider)"/>
  </svg>
  <div class="range-ends"><span>0</span><span>30 years</span></div>
  <div class="field" style="top:253px">One time payout</div>
  <div class="or">OR</div>
  <div class="field" style="top:350px">Monthly payment</div>
  <a class="invest" href="#">I want to invest</a>
</section>

<footer class="site-footer">
  <nav class="footer-nav">
    <a href="#">About Us</a><span class="sep">|</span><a href="#">FAQ</a><span class="sep">|</span><a href="#">Privacy Policy</a><span class="sep">|</span><a href="#">Contact</a>
  </nav>
  <p class="copyright">Copyright © 2017&nbsp; All Rights Reserved</p>
</footer>
</body>
</html>
```